Top Scottish IT Company - Web Banner

We want a banner for our main web page that graphically conveys the following values for our IT support company (in the priority order listed)....

a. Secure (your network will be)
b. Pro-Active (management of IT)
c. Expert (in IT systems)
d. Reliable (your network will be)
e. Innovative (our approach is)

Note - I do not want the list of text above to be simply listed in the design - I want them to be inferred by the design - so far as is possible.

The strap line "Expert in maintaing reliable and secure IT networks" - or very similar.

Size of image = 967*240 pixels.

Company Name - Dunmore Systems Ltd - named after the explorer Tobias Dunmore (Current Website = www.dunsysnet.co.uk)

The brief has been updated in light of the first few responses that relied too heavily on the text - it is a banner image we preffer not simply a rpetition of the text in the breif.

Hope this helps.
Neville

Target Market(s)

UK based SME's with large investment in and dependency on IT.

Industry/Entity Type

It Company

Requirements
Must have
• Must Portray IT Secuirty and ProActive apporach to IT management.

```html
<!DOCTYPE html>
<html lang="en">
<head>
<meta charset="utf-8">
<title>Dunmore Systems Ltd – Web Banner</title>
<link href="https://fonts.googleapis.com/css2?family=PT+Sans:wght@700&display=swap" rel="stylesheet">
<style>
  :root {
    --teal-light: #b4d3c5;
    --teal-mid: #7fb3a6;
    --teal-deep: #4f8f8a;
    --blue-bright: #2f8ce0;
    --blue-deep: #0c5cb4;
    --shield-blue: #1d6fd0;
    --shield-edge: #0b3f86;
    --white: #ffffff;
    --glow: rgba(255, 255, 255, 0.85);
    --lock-steel: #8a9aa0;
    --lock-dark: #2b3236;
  }
  html, body {
    margin: 0;
    padding: 0;
    width: 1200px;
    height: 298px;
    overflow: hidden;
    background: var(--white);
  }
  .banner {
    position: relative;
    width: 1200px;
    height: 298px;
    overflow: hidden;
    font-family: "PT Sans", "Trebuchet MS", sans-serif;
    font-weight: 700;
    color: var(--white);
    background: linear-gradient(100deg, var(--teal-light) 0%, var(--teal-mid) 35%, var(--teal-deep) 100%);
  }
  .blue-band {
    position: absolute;
    left: 0;
    top: 168px;
    width: 1200px;
    height: 130px;
    background: linear-gradient(90deg, rgba(47,140,224,0) 8%, rgba(47,140,224,0.85) 24%, var(--blue-bright) 45%, var(--blue-deep) 100%);
  }
  .padlock-art {
    position: absolute;
    left: 37px;
    top: 6px;
    width: 143px;
    height: 279px;
    border-radius: 18px 18px 10px 10px;
    background: linear-gradient(180deg, var(--lock-steel) 0%, #dfe6e8 55%, var(--lock-dark) 100%);
  }
  .values {
    position: absolute;
    left: 232px;
    top: 0;
    margin: 0;
    padding: 0;
    list-style: none;
  }
  .value {
    position: absolute;
    left: 0;
    display: flex;
    align-items: center;
    white-space: nowrap;
    font-size: 27px;
    letter-spacing: -0.2px;
    text-shadow: 0 0 6px var(--glow), 0 0 2px var(--glow);
    transform: translateY(-50%);
  }
  .value svg { width: 30px; height: 34px; margin-right: 21px; flex: none; }
  .value-secure { top: 58px; }
  .value-proactive { top: 99px; }
  .value-expert { top: 146px; }
  .value-reliable { top: 199px; }
  .value-innovative { top: 240px; }

  .swoosh {
    position: absolute;
    left: 600px;
    top: 40px;
    width: 600px;
    height: 140px;
  }
  .tagline {
    position: absolute;
    left: 918px;
    top: 68px;
    margin: 0;
    transform: translateX(-50%);
    width: 460px;
    text-align: center;
    font-size: 26px;
    line-height: 33px;
    text-shadow: 0 0 6px var(--glow), 0 0 2px var(--glow);
  }
  .brand {
    position: absolute;
    left: 707px;
    top: 187px;
    display: flex;
    align-items: center;
    height: 90px;
  }
  .brand-dot {
    width: 88px;
    height: 88px;
    border-radius: 50%;
    background: var(--white);
    opacity: 0.9;
    margin-right: 32px;
  }
  .brand-name {
    font-size: 36px;
    letter-spacing: 1px;
    color: var(--white);
    white-space: nowrap;
  }
</style>
</head>
<body>
<div class="banner">
  <div class="blue-band"></div>

  <div class="padlock-art" role="img" aria-label="Illustration of an open steel padlock with a striped base"></div>

  <svg width="0" height="0" style="position:absolute">
    <defs>
      <symbol id="shield-tick" viewBox="0 0 30 34">
        <path d="M15 1 L28 5 V16 C28 25 22 30 15 33 C8 30 2 25 2 16 V5 Z" fill="var(--shield-blue)" stroke="var(--shield-edge)" stroke-width="2"/>
        <path d="M8 17 L13 22 L23 10" fill="none" stroke="var(--white)" stroke-width="4" stroke-linecap="round" stroke-linejoin="round"/>
      </symbol>
    </defs>
  </svg>

  <ul class="values">
    <li class="value value-secure"><svg><use href="#shield-tick"/></svg>Secure Networks</li>
    <li class="value value-proactive"><svg><use href="#shield-tick"/></svg>Pro_Active Maintenance</li>
    <li class="value value-expert"><svg><use href="#shield-tick"/></svg>Expert Technicians</li>
    <li class="value value-reliable"><svg><use href="#shield-tick"/></svg>Reliable Systems</li>
    <li class="value value-innovative"><svg><use href="#shield-tick"/></svg>Innovative Approach</li>
  </ul>

  <svg class="swoosh" viewBox="0 0 600 140" aria-hidden="true">
    <path d="M110 120 C250 130 420 110 600 60" fill="none" stroke="rgba(255,255,255,0.9)" stroke-width="2.5"/>
    <path d="M130 126 C280 138 440 115 600 75" fill="none" stroke="rgba(255,255,255,0.5)" stroke-width="1.5"/>
    <path d="M110 120 C60 112 40 100 70 90" fill="none" stroke="rgba(255,255,255,0.7)" stroke-width="1.5"/>
  </svg>

  <p class="tagline">"Expert in maintaing reliable<br>and secure IT networks"</p>

  <div class="brand">
    <span class="brand-dot"></span>
    <span class="brand-name">Dunmore Systems Ltd</span>
  </div>
</div>
</body>
</html>
```